Gebrauchtwagenhandel sucht Logo & Visitenkarte
Very good & quick response on all our wishes and ideas. I would like to recommend the designer for his daily constant efforts to work it out - very nice !!
Zielgruppe
Wir betreiben einen Gebrauchtwagenhandel.
Aufgabenstellung
1) Wir möchten das kaufmännische '&' in einer kleineren 2/3 Proportion zu den Buchstaben 'B' & 'G'. Allerdings ohne Freizeichen zusammengeschrieben.
2) Wir möchten ein Logo mit einem vertrauensbildenden Charakter erhalten.
3) Wir möchten nicht eines von diesen Kfz Silhouetten in unserem Logo haben, mit dem jeder zweite Händler antritt.
4) Unsere Rechtsform 'GmbH & Co. KG' soll sich dezent, wie auch immer, auf oder um das Logo bzw. Visitenkarte wiederfinden.
5) Für die Visitenkarten sollen folgende Punkte/Zeilen eingefügt werden ( zwei Geschäftsführer):
- Internetadresse (Nachtrag)
- Email Adresse (Nachtrag)
- Festnetz Nummer (Nachtrag)
- Mobile Nummer (Nachtrag)

```html
<!DOCTYPE html>
<html lang="de">
<head>
<meta charset="utf-8">
<title>Velmar Automobile – Visitenkarten</title>
<link rel="stylesheet" href="https://fonts.googleapis.com/css2?family=Roboto:wght@300;400&display=swap">
<style>
  :root {
    --backdrop: #b3b3b3;
    --shadow: #666666;
    --paper: #f2f2f2;
    --navy: #173559;
    --icon-blue: #1d4f8a;
    --ink: #333333;
    --rule: #2b2b2b;
    --band-grey: #8a8a8b;
    --logo-light: #c8c8c8;
    --logo-grey: #a9a9a9;
    --white: #ffffff;
  }
  * { margin: 0; padding: 0; box-sizing: border-box; }
  html, body {
    width: 1200px; height: 1099px; overflow: hidden;
    background: var(--backdrop);
    font-family: "Roboto", Arial, sans-serif;
    font-weight: 300;
    color: var(--ink);
  }
  .sheet { position: relative; width: 1200px; height: 1099px; }

  .card {
    position: absolute; width: 525px; height: 307px;
    background: var(--paper);
    box-shadow: 12px 12px 0 var(--shadow);
    overflow: hidden;
  }
  .card--navy { background: var(--navy); }
  .col-left { left: 58px; }
  .col-right { left: 618px; }
  .row-1 { top: 58px; }
  .row-2 { top: 396px; }
  .row-3 { top: 734px; }

  .abs { position: absolute; }

  /* brand name stand-in */
  .brand {
    position: absolute; display: flex; align-items: center; gap: 10px;
    font-weight: 400; color: var(--navy); white-space: nowrap;
  }
  .brand__square { display: block; background: var(--navy); }
  .brand--small { font-size: 26px; }
  .brand--small .brand__square { width: 22px; height: 22px; }
  .brand--large { font-size: 38px; gap: 14px; }
  .brand--large .brand__square { width: 32px; height: 32px; }
  .brand--light { color: var(--logo-light); }
  .brand--light .brand__square { background: var(--logo-light); }
  .brand--grey { color: var(--logo-grey); }
  .brand--grey .brand__square { background: var(--logo-grey); }

  .person-name { font-weight: 300; color: var(--navy); font-size: 29px; line-height: 1; white-space: nowrap; }
  .person-role { font-size: 15px; line-height: 1; white-space: nowrap; }

  .address { font-size: 16px; line-height: 19px; }
  .icon { width: 16px; height: 16px; fill: var(--icon-blue); display: block; }
  .icon--pin { width: 14px; height: 19px; }

  .contact-list { list-style: none; font-size: 15.5px; }
  .contact-list li { display: flex; align-items: center; height: 22.5px; white-space: nowrap; }
  .contact-list--left li { gap: 18px; }
  .contact-list--right li { justify-content: flex-end; gap: 12px; }

  .rule { position: absolute; height: 1px; background: var(--rule); }
  .accent-bar { position: absolute; left: 0; top: 100px; width: 8px; height: 78px; background: var(--navy); }

  .url {
    position: absolute; left: 0; right: 0; text-align: center;
    font-weight: 400; font-size: 19px; letter-spacing: 1.6px;
  }
  .url--dark { color: var(--ink); }
  .url--white { color: var(--white); }
  .url--grey { color: var(--logo-grey); }
</style>
</head>
<body>
<svg width="0" height="0" style="position:absolute" aria-hidden="true">
  <symbol id="i-pin" viewBox="0 0 14 19"><path d="M7 0a7 7 0 0 0-7 7c0 5 7 12 7 12s7-7 7-12a7 7 0 0 0-7-7zm0 10a3 3 0 1 1 0-6 3 3 0 0 1 0 6z"/></symbol>
  <symbol id="i-phone" viewBox="0 0 20 16"><path d="M1 6c0-3 4-5 9-5s9 2 9 5h-5V4H6v2H1zM5 7h10l3 8H2l3-8zm3 2v1h1V9H8zm2 0v1h1V9h-1zm2 0v1h1V9h-1zM8 11v1h1v-1H8zm2 0v1h1v-1h-1zm2 0v1h1v-1h-1z"/></symbol>
  <symbol id="i-mobile" viewBox="0 0 12 20"><path d="M2 0h8a2 2 0 0 1 2 2v16a2 2 0 0 1-2 2H2a2 2 0 0 1-2-2V2a2 2 0 0 1 2-2zm0 3v7h8V3H2zm1 9v1.5h1.5V12H3zm2.3 0v1.5h1.5V12H5.3zm2.2 0v1.5H9V12H7.5zM3 14.5V16h1.5v-1.5H3zm2.3 0V16h1.5v-1.5H5.3zm2.2 0V16H9v-1.5H7.5z"/></symbol>
  <symbol id="i-mail" viewBox="0 0 18 12"><path d="M0 0h18v12H0V0zm1.5 1.3v9.4L6.5 6 1.5 1.3zm15 0L11.5 6l5 4.7V1.3zM2.6 1 9 7l6.4-6H2.6zm4.9 5.9L2.6 11h12.8l-4.9-4.1L9 8.3 7.5 6.9z"/></symbol>
  <symbol id="i-globe" viewBox="0 0 18 18"><path d="M9 0a9 9 0 1 0 0 18A9 9 0 0 0 9 0zm-.7 1.6V5H5.6c.6-1.8 1.6-3 2.7-3.4zm1.4 0c1.1.4 2.1 1.6 2.7 3.4H9.7V1.6zM5.3 6.3h3v2H5.1c0-.7.1-1.4.2-2zm4.4 0h3c.1.6.2 1.3.2 2H9.7v-2zM1.5 8.3c.1-.7.3-1.4.6-2h1.9c-.1.6-.2 1.3-.2 2H1.5zm12.7 0c0-.7-.1-1.4-.2-2h1.9c.3.6.5 1.3.6 2h-2.3zM1.5 9.7h2.3c0 .7.1 1.4.2 2H2.1c-.3-.6-.5-1.3-.6-2zm3.6 0h3.2v2h-3c-.1-.6-.2-1.3-.2-2zm4.6 0h3.2c0 .7-.1 1.4-.2 2h-3v-2zm4.5 0h2.3c-.1.7-.3 1.4-.6 2H14c.1-.6.2-1.3.2-2zM5.6 13h2.7v3.4c-1.1-.4-2.1-1.6-2.7-3.4zm4.1 0h2.7c-.6 1.8-1.6 3-2.7 3.4V13z"/></symbol>
</svg>

<main class="sheet">

  <!-- Front A -->
  <section class="card col-left row-1">
    <div class="brand brand--small" style="left:212px; top:52px;"><span class="brand__square"></span>Velmar Automobile</div>
    <span class="accent-bar"></span>
    <p class="person-name abs" style="left:29px; top:116px;">Lorenz Haberfeld</p>
    <p class="person-role abs" style="left:30px; top:147px;">Managing Director</p>
    <svg class="icon icon--pin abs" style="left:34px; top:200px;"><use href="#i-pin"/></svg>
    <p class="address abs" style="left:58px; top:199px;">Lindenweg 12<br>24568 Halmstedt</p>
    <ul class="contact-list contact-list--left abs" style="left:289px; top:194px;">
      <li><svg class="icon"><use href="#i-phone"/></svg>[040] 21987 6540</li>
      <li><svg class="icon"><use href="#i-mobile"/></svg>[040] 21987 6540</li>
      <li><svg class="icon"><use href="#i-mail"/></svg>info@velmar-auto.de</li>
      <li><svg class="icon"><use href="#i-globe"/></svg>www.velmar-auto.de</li>
    </ul>
  </section>

  <!-- Back A -->
  <section class="card col-right row-1">
    <div class="brand brand--large" style="left:81px; top:127px;"><span class="brand__square"></span>Velmar Automobile</div>
    <p class="url url--dark" style="top:258px;">www.velmar-auto.de</p>
  </section>

  <!-- Front B -->
  <section class="card col-left row-2">
    <div class="brand brand--small" style="left:36px; top:50px;"><span class="brand__square"></span>Velmar Automobile</div>
    <p class="person-name abs" style="right:35px; top:120px;">Deniz Karaman</p>
    <span class="rule" style="left:36px; right:0; top:153px;"></span>
    <p class="person-role abs" style="right:36px; top:161px;">Managing Director</p>
    <svg class="icon icon--pin abs" style="left:35px; top:208px;"><use href="#i-pin"/></svg>
    <p class="address abs" style="left:59px; top:207px;">Lindenweg 12<br>24568 Halmstedt</p>
    <ul class="contact-list contact-list--right abs" style="right:36px; top:205px;">
      <li>[040] 21987 6540<svg class="icon"><use href="#i-phone"/></svg></li>
      <li>[040] 21987 6540<svg class="icon"><use href="#i-mobile"/></svg></li>
      <li>info@velmar-auto.de<svg class="icon"><use href="#i-mail"/></svg></li>
      <li>www.velmar-auto.de<svg class="icon"><use href="#i-globe"/></svg></li>
    </ul>
  </section>

  <!-- Back B -->
  <section class="card card--navy col-right row-2">
    <div class="brand brand--large brand--light" style="left:81px; top:127px;"><span class="brand__square"></span>Velmar Automobile</div>
    <p class="url url--white" style="top:258px;">www.velmar-auto.de</p>
  </section>

  <!-- Front C -->
  <section class="card col-left row-3">
    <div class="brand brand--small" style="left:32px; top:44px;"><span class="brand__square"></span>Velmar Automobile</div>
    <span class="rule" style="left:0; width:290px; top:100px;"></span>
    <p class="person-name abs" style="left:126px; top:156px; transform:translateX(-50%);">Lorenz Haberfeld</p>
    <p class="person-role abs" style="left:126px; top:186px; transform:translateX(-50%);">Managing Director</p>
    <ul class="contact-list contact-list--right abs" style="right:22px; top:126px;">
      <li style="height:auto; align-items:flex-start;"><span class="address" style="text-align:right;">Lindenweg 12<br>24568 Halmstedt</span><svg class="icon icon--pin" style="margin:2px 1px 0 1px;"><use href="#i-pin"/></svg></li>
      <li style="margin-top:4px;">[040] 21987 6540<svg class="icon"><use href="#i-phone"/></svg></li>
      <li>[040] 21987 6540<svg class="icon"><use href="#i-mobile"/></svg></li>
      <li>info@velmar-auto.de<svg class="icon"><use href="#i-mail"/></svg></li>
      <li>www.velmar-auto.de<svg class="icon"><use href="#i-globe"/></svg></li>
    </ul>
    <svg class="abs" style="left:0; top:277px;" width="525" height="30" viewBox="0 0 525 30" aria-hidden="true">
      <polygon points="0,0 333,0 300,30 0,30" fill="var(--band-grey)"/>
      <polygon points="344,0 525,0 525,30 309,30" fill="var(--navy)"/>
    </svg>
  </section>

  <!-- Back C -->
  <section class="card card--navy col-right row-3">
    <div class="brand brand--large brand--grey" style="left:81px; top:127px;"><span class="brand__square"></span>Velmar Automobile</div>
    <p class="url url--grey" style="top:258px;">www.velmar-auto.de</p>
  </section>

</main>
</body>
</html>
```